Design the best Halloween flyer

Hi everyone, I am looking for a Halloween design for a club flyer. Here are the details to be included on the flyer for this event...

Company Name - Velvet Orbit Ent Presents
Event Name - Crimson Howl
Event Date - TBD
Music By - DJ Marlow (Playing nothing but the Hottest!! Pop, Hip Hop, Reggeaton, Salsa, Reggea , House, and so much more!!)
Extra Curricular Activities - Best Costume Cash Grand Prize
Event Details - Doors Open at 9pm, 21+ Event/ Proper ID is a Must, For More Info Call (508)-555-0187
Social Media -FB [login to view URL]
INS [login to view URL]
Venue - THE CORVEL 17 Bramble Ln. Nantucket MA 02554

I've attached two images of flyers that some what resemble what I'm looking for, but feel free to get creative and come up with your own design, the best design will win out. Thank you all for your time, and good luck ;)...

```html
<!DOCTYPE html>
<html lang="en">
<head>
<meta charset="utf-8">
<title>Crimson Howl – Halloween Flyer</title>
<link href="https://fonts.googleapis.com/css2?family=Rubik+Dirt&family=Oswald:wght@400;500;700&family=Yellowtail&display=swap" rel="stylesheet">
<style>
  :root {
    --page: #d9d9d9;
    --ink: #121212;
    --char: #2a2a2a;
    --ember: #d9521f;
    --flame: #f39a3c;
    --blood: #e3262b;
    --bone: #f2f2f2;
  }
  * { box-sizing: border-box; margin: 0; padding: 0; }
  html, body { width: 1200px; height: 800px; overflow: hidden; }
  body { background: var(--page); font-family: "Oswald", sans-serif; }

  .flyer {
    position: absolute; left: 340px; top: 36px;
    width: 520px; height: 728px;
    background: var(--ink);
    overflow: hidden;
    box-shadow: 0 10px 30px rgba(0,0,0,.35);
    text-align: center;
    color: var(--bone);
  }
  .flyer__backdrop {
    position: absolute; inset: 0;
    background:
      linear-gradient(90deg, rgba(217,82,31,.55), transparent 14%, transparent 86%, rgba(217,82,31,.55)),
      linear-gradient(0deg, rgba(243,154,60,.45), transparent 18%),
      radial-gradient(ellipse 70% 45% at 50% 62%, var(--char), var(--ink) 85%);
  }
  .flyer__skull {
    position: absolute; left: 90px; top: 60px;
    width: 340px; height: 270px;
    background:
      radial-gradient(ellipse 30% 42% at 50% 48%, #bfb4a6, #6e6258 60%, transparent 80%),
      radial-gradient(ellipse 22% 30% at 22% 22%, rgba(243,154,60,.8), transparent 75%),
      radial-gradient(ellipse 22% 30% at 78% 22%, rgba(243,154,60,.8), transparent 75%),
      radial-gradient(ellipse 18% 26% at 12% 90%, rgba(217,82,31,.8), transparent 75%),
      radial-gradient(ellipse 18% 26% at 88% 90%, rgba(217,82,31,.8), transparent 75%);
  }
  .flyer__content { position: relative; }

  .presenter { margin-top: 18px; font-size: 9px; letter-spacing: 2px; font-weight: 500; }
  .presenter__brand { font-size: 12px; color: var(--blood); font-weight: 700; letter-spacing: 1px; }

  .event-title { margin-top: 262px; line-height: 1; font-weight: 400; }
  .event-title__main {
    display: block; font-family: "Rubik Dirt", sans-serif;
    font-size: 74px; letter-spacing: 1px; color: var(--bone);
  }
  .event-title__script {
    display: block; margin-top: -18px;
    font-family: "Yellowtail", cursive; font-size: 58px;
    color: var(--flame); text-shadow: 0 0 8px rgba(217,82,31,.7);
  }

  .event-date { margin-top: 2px; font-size: 30px; font-weight: 500; letter-spacing: 1px; }
  .event-date__label { color: var(--blood); }

  .dj-name { font-size: 30px; font-weight: 700; color: var(--blood); line-height: 1.1; }

  .divider { display: block; margin: 6px auto 4px; }

  .detail { font-size: 13px; font-weight: 500; letter-spacing: .3px; line-height: 1.85; }
  .detail__label { color: var(--blood); }
  .detail__sep { color: var(--blood); margin: 0 8px; }

  .social { margin-top: 12px; font-size: 14px; font-weight: 500; }
  .social__fb { color: var(--blood); }
  .social__bar { color: var(--bone); margin: 0 6px; }
</style>
</head>
<body>
  <article class="flyer">
    <div class="flyer__backdrop" role="img" aria-label="Dark smoky background with flames burning along the edges"></div>
    <div class="flyer__skull" role="img" aria-label="Halloween horror skull wreathed in flames"></div>

    <div class="flyer__content">
      <p class="presenter">PRESENTS BY:</p>
      <p class="presenter__brand">VELVET ORBIT ENT</p>

      <h1 class="event-title">
        <span class="event-title__main">CRIMSON</span>
        <span class="event-title__script">Howl</span>
      </h1>

      <p class="event-date"><span class="event-date__label">DATE</span> TBD</p>
      <p class="dj-name">DJ MARLOW</p>

      <svg class="divider" width="300" height="8" viewBox="0 0 300 8" aria-hidden="true">
        <line x1="0" y1="4" x2="135" y2="4" stroke="#f2f2f2" stroke-width="1" stroke-dasharray="6 5"/>
        <circle cx="150" cy="4" r="3" fill="#e3262b"/>
        <line x1="165" y1="4" x2="300" y2="4" stroke="#f2f2f2" stroke-width="1" stroke-dasharray="6 5"/>
      </svg>

      <p class="detail">POP, HIP HOP, REGGETON, SALSA, REGGEA , HOUSE, AND SO MUCH MORE!!</p>
      <p class="detail"><span class="detail__label">EXTRA CURRICULAR ACTIVITIES</span> - BEST COSTUME CASH GRAND PRIZE</p>
      <p class="detail">DOOR OPEN <span class="detail__label">9PM</span><span class="detail__sep">×</span>CALL : (508)-555-0187</p>
      <p class="detail"><span class="detail__label">21+ EVENT</span> - PROPER ID IS A MUST</p>
      <p class="detail"><span class="detail__label">VENUE</span> - THE CORVEL 17 BRAMBLE LN. NANTUCKET MA 02554</p>

      <p class="social"><span class="social__fb">FACEPAGE.NET/VELVETORBITENT</span><span class="social__bar">|</span>SNAPGRAM.NET/VELVETORBITENT</p>
    </div>
  </article>
</body>
</html>
```